Criação de Folder para Planejamento de Eventos
" Nós trabalhamos com eventos de adultos, eventos infantis e também nos flexibilizamos para locação de nosso espaço, sem nosso buffet. "

```html
<!DOCTYPE html>
<html lang="pt-BR">
<head>
<meta charset="utf-8">
<title>Folder – Aurora Eventos</title>
<link rel="stylesheet" href="https://fonts.googleapis.com/css2?family=Cinzel:wght@600&display=swap">
<style>
  :root {
    --page-bg: #ececec;
    --cover-bg: #dccab2;
    --cover-glow: #efe3d2;
    --brand-red: #c3272f;
    --brand-red-soft: rgba(195, 39, 47, 0.55);
    --brand-brown-soft: rgba(91, 70, 54, 0.45);
  }
  * { margin: 0; padding: 0; box-sizing: border-box; }
  html, body {
    width: 1200px;
    height: 1200px;
    overflow: hidden;
    background: var(--page-bg);
  }
  .folder-cover {
    position: absolute;
    left: 200px;
    top: 40px;
    width: 800px;
    height: 1120px;
    background: radial-gradient(circle at 58% 42%, var(--cover-glow) 0%, var(--cover-bg) 70%);
    overflow: hidden;
    box-shadow: 0 6px 24px rgba(0,0,0,0.12);
  }
  .cover-artwork {
    position: absolute;
    inset: 0;
    background:
      radial-gradient(ellipse 60% 55% at 0% 20%, var(--brand-red-soft) 0%, rgba(195,39,47,0) 100%),
      radial-gradient(ellipse 70% 60% at 10% 85%, var(--brand-brown-soft) 0%, rgba(91,70,54,0) 100%),
      radial-gradient(ellipse 45% 40% at 35% 100%, var(--brand-red-soft) 0%, rgba(195,39,47,0) 100%);
  }
  .brand-signature {
    position: absolute;
    right: 130px;
    bottom: 150px;
    display: flex;
    flex-direction: column;
    align-items: center;
    gap: 6px;
  }
  .brand-dot {
    width: 46px;
    height: 46px;
    border-radius: 50%;
    background: var(--brand-red);
  }
  .brand-name {
    font-family: "Cinzel", serif;
    font-weight: 600;
    font-size: 34px;
    letter-spacing: 2px;
    color: var(--brand-red);
    line-height: 1;
  }
  .brand-tagline {
    font-family: "Cinzel", serif;
    font-weight: 600;
    font-size: 11px;
    letter-spacing: 3px;
    color: var(--brand-red);
    line-height: 1;
  }
</style>
</head>
<body>
  <main class="folder-cover">
    <div class="cover-artwork" role="img" aria-label="Decorative sweep of red and brown curved bands across the left side of the cover"></div>

    <div class="brand-signature">
      <div class="brand-dot"></div>
      <div class="brand-name">AURORA</div>
      <div class="brand-tagline">EVENTOS &amp; RECEPÇÕES</div>
    </div>
  </main>
</body>
</html>
```